The Jawline Remedy Business Card

Looking for a business card design: front and back. It will be printed at presspanda.example on a leaf cutout trifecta paper with green middle. 3.5 x 2 leaf cutout. It will need bleed room around edges. The front will have my picture, logo, website and email address. The back will be a quote. "Finally. The complete solution to helping you open your mouth fully without pain"
and
"Like Us on Chatterbox to Learn More @ The Jawline Remedy"

Target Market(s)

Women 20-55 years old

Industry/Entity Type

Health Service

Contact Information for Business Card

My photo on one side or embedded, Name: Dr. Marlon Quaid, PT, DPT, MS Website: TheJawlineRemedy.example Email: marlon@keystonemotionclinic.example

Requirements
Must have
• Unique design consistent with my logo

```html
<!DOCTYPE html>
<html lang="en">
<head>
<meta charset="utf-8">
<title>The Jawline Remedy — Business Card</title>
<link rel="stylesheet" href="https://fonts.googleapis.com/css2?family=Roboto:wght@400;500;700&display=swap">
<style>
  :root {
    --backdrop: #2b2b2b;
    --brand-blue: #1076bf;
    --brand-green: #8cc63f;
    --paper: #ffffff;
    --photo-light: #c9d3de;
    --photo-dark: #6f7f92;
  }
  * { margin: 0; padding: 0; box-sizing: border-box; }
  html, body {
    width: 1125px;
    height: 1200px;
    overflow: hidden;
    background: var(--backdrop);
    font-family: "Roboto", Arial, sans-serif;
  }
  .canvas { position: relative; width: 1125px; height: 1200px; }

  .card {
    position: absolute;
    left: 171px;
    width: 825px;
    height: 469px;
    overflow: hidden;
  }
  .card-front {
    top: 107px;
    background: var(--paper);
    border-top-left-radius: 135px;
    border-bottom-right-radius: 135px;
  }
  .card-back {
    top: 640px;
    background: var(--brand-blue);
    border-top-right-radius: 140px;
    border-bottom-left-radius: 140px;
  }

  .wave { position: absolute; inset: 0; width: 825px; height: 469px; }

  .brand {
    position: absolute;
    left: 56px;
    top: 82px;
    display: flex;
    align-items: center;
    gap: 22px;
  }
  .brand-circle {
    width: 150px; height: 150px;
    border: 6px solid var(--brand-blue);
    border-radius: 50%;
  }
  .brand-name {
    color: var(--brand-green);
    font-weight: 700;
    font-size: 40px;
    line-height: 1.02;
  }

  .portrait {
    position: absolute;
    left: 618px; top: 73px;
    width: 150px; height: 172px;
    border-radius: 16px;
    border: 1px solid #d6d6d6;
    background: linear-gradient(180deg, var(--photo-light), var(--photo-dark));
  }

  .contact {
    position: absolute;
    right: 54px;
    top: 256px;
    text-align: right;
    color: var(--paper);
  }
  .contact-name { font-size: 27px; font-weight: 700; line-height: 34px; }
  .contact-credentials { font-size: 27px; font-weight: 700; line-height: 34px; margin-bottom: 10px; }
  .contact-line { font-size: 17.5px; line-height: 24px; }

  .back-mark {
    position: absolute;
    left: 280px; top: 80px;
    width: 250px; height: 250px;
    border: 7px solid var(--paper);
    border-radius: 50%;
    display: flex; align-items: center; justify-content: center;
    text-align: center;
  }
  .back-mark-name {
    color: var(--paper);
    font-weight: 700;
    font-size: 34px;
    line-height: 1.1;
  }

  .tagline {
    position: absolute;
    left: 62px; width: 685px;
    top: 369px;
    text-align: center;
    color: var(--paper);
    font-size: 14.5px;
    font-weight: 500;
    text-transform: uppercase;
    padding-bottom: 3px;
    border-bottom: 1.5px solid var(--paper);
  }
  .tagline strong { font-weight: 700; }
  .follow {
    position: absolute;
    left: 0; width: 810px;
    top: 404px;
    text-align: center;
    color: var(--paper);
    font-size: 14.5px;
  }
</style>
</head>
<body>
<main class="canvas">
  <section class="card card-front">
    <svg class="wave" viewBox="0 0 825 469" aria-hidden="true">
      <path d="M0 330 C150 392 300 418 430 330 S660 150 825 122" fill="none" stroke="var(--brand-green)" stroke-width="14"/>
      <path d="M0 360 C150 430 300 450 430 352 S660 165 825 138" fill="none" stroke="var(--brand-blue)" stroke-width="6"/>
      <path d="M0 380 C150 448 300 460 440 365 S660 172 825 145 L825 469 L0 469 Z" fill="var(--brand-blue)"/>
    </svg>

    <div class="brand">
      <div class="brand-circle"></div>
      <div class="brand-name">The<br>Jawline<br>Remedy</div>
    </div>

    <div class="portrait" role="img" aria-label="Portrait photo of Dr. Marlon Quaid"></div>

    <div class="contact">
      <p class="contact-name">Dr. Marlon Quaid</p>
      <p class="contact-credentials">PT, DPT, MS</p>
      <p class="contact-line">555-014-2287</p>
      <p class="contact-line">marlon@keystonemotionclinic.example</p>
      <p class="contact-line">www.TheJawlineRemedy.example</p>
    </div>
  </section>

  <section class="card card-back">
    <div class="back-mark">
      <p class="back-mark-name">The<br>Jawline<br>Remedy</p>
    </div>
    <p class="tagline">Finally. The complete solution to helping you <strong>open your mouth fully without pain</strong></p>
    <p class="follow">Like Us on Chatterbox to Learn More @ The Jawline Remedy</p>
  </section>
</main>
</body>
</html>
```